Living with Silverwattle Care NT proudly supporting QCSP services.

Flyer required promoting all of our services listed on the attached flyer
Silverwattle Care provides the below services:
Day Programs for capacity building
Respite experiences.
Community access & in- home supports
Support workers
Supported Independant Living
Customised Employment

```html
<!DOCTYPE html>
<html lang="en">
<head>
<meta charset="utf-8">
<title>Living with Silverwattle Care NT</title>
<link rel="stylesheet" href="https://fonts.googleapis.com/css2?family=Rubik:wght@400;500;700;800&family=Sacramento&display=swap">
<style>
  :root {
    --purple: #8e3a80;
    --purple-deep: #6b2a6e;
    --plum: #5e1f4f;
    --yellow: #f7db00;
    --yellow-text: #f5e000;
    --yellow-heart: #e6c800;
    --teal: #3ccfae;
    --ink: #1c1c1c;
    --paper: #ffffff;
    --lilac: #c79ac0;
    --pale-yellow: #f9ec8c;
    --pale-teal: #a6ebdc;
  }
  * { box-sizing: border-box; margin: 0; padding: 0; }
  html, body { width: 899px; height: 1200px; overflow: hidden; background: var(--paper); }
  .flyer {
    position: relative; width: 899px; height: 1200px; overflow: hidden;
    background: var(--paper); font-family: "Rubik", sans-serif; color: var(--ink);
  }
  .backdrop { position: absolute; inset: 0; }

  .brand {
    position: absolute; left: 47px; top: 76px;
    display: flex; align-items: center; gap: 12px;
    font: 700 32px/1 "Rubik", sans-serif; color: var(--purple);
  }
  .brand-dot { width: 40px; height: 40px; border-radius: 50%; background: var(--purple); flex: none; }

  .title { position: absolute; left: 48px; top: 214px; }
  .title-main { display: block; font: 800 52px/1 "Rubik", sans-serif; color: var(--ink); letter-spacing: -0.5px; }
  .title-script { display: block; font: 400 66px/1 "Sacramento", cursive; color: var(--teal); margin-top: 2px; }

  .photo { position: absolute; border: 4px solid; border-radius: 8px; }
  .photo-sewing { left: 431px; top: 40px; width: 216px; height: 184px; transform: rotate(-5deg); border-color: var(--teal); background: linear-gradient(135deg, #d8d2c6, #8e8678 60%, #3c3c40); }
  .photo-craft { left: 650px; top: 46px; width: 208px; height: 174px; border-color: var(--yellow); background: linear-gradient(135deg, #6d5a45, #6b5cb0 55%, #4a3f6e); }
  .photo-card { left: 630px; top: 210px; width: 222px; height: 180px; transform: rotate(5deg); border-color: var(--purple); background: linear-gradient(135deg, #d9c8b5, #4d6fb5 55%, #f1e6e6); }
  .photo-kitchen { left: 446px; top: 760px; width: 236px; height: 196px; transform: rotate(-8deg); border: 4px solid var(--paper); background: linear-gradient(135deg, #8a6a4e, #c7b8a8 50%, #2e2a28); }
  .photo-group { left: 676px; top: 730px; width: 228px; height: 218px; transform: rotate(8deg); border: 4px solid var(--paper); background: linear-gradient(135deg, #d8c9a8, #a4514a 50%, #3d6b72); }
  .partner-badge { position: absolute; left: 498px; top: 200px; width: 144px; height: 144px; border-radius: 50%; background: var(--purple-deep); }

  .services-panel {
    position: absolute; left: 46px; top: 389px; width: 404px; height: 771px;
    background: var(--purple); border-bottom-right-radius: 90px; color: var(--paper);
  }
  .service { position: absolute; left: 24px; width: 364px; }
  .service-title { font: 700 18.5px/22px "Rubik", sans-serif; color: var(--yellow-text); }
  .script { font: 400 25px/0 "Sacramento", cursive; color: var(--teal); }
  .service-body { font: 400 13.4px/17px "Rubik", sans-serif; margin-top: 10px; }
  .service-day { top: 16px; }
  .service-respite { top: 245px; }
  .service-community { top: 417px; }
  .service-employment { top: 603px; }

  .services-right { position: absolute; left: 476px; top: 0; width: 366px; }
  .services-right .service { left: 0; width: 366px; }
  .services-right .service-title { color: var(--purple); }
  .services-right .service-body { color: var(--ink); }
  .service-workers { top: 395px; }
  .service-living { top: 585px; }

  .contact {
    position: absolute; left: 469px; top: 964px; width: 430px; height: 196px;
    background: var(--yellow); border-top-right-radius: 120px;
    padding: 26px 0 0 24px; color: var(--ink);
  }
  .contact-title { font: 700 28px/1 "Rubik", sans-serif; color: var(--purple-deep); }
  .contact-line { display: flex; align-items: flex-start; gap: 8px; font: 400 18px/20px "Rubik", sans-serif; margin-top: 8px; }
  .contact-line svg { flex: none; margin-top: 4px; }
  .social-title { font: 700 14px/1 "Rubik", sans-serif; color: var(--purple-deep); margin-top: 12px; }
  .social-title .script { font-size: 22px; color: var(--purple-deep); }
  .social-list { display: flex; gap: 10px; margin-top: 12px; list-style: none; }
  .social-list li { width: 13px; height: 13px; border-radius: 50%; background: var(--purple-deep); }

  .heart { position: absolute; border-radius: 50%; }
  .heart-teal { left: 408px; top: 146px; width: 58px; height: 50px; background: var(--teal); }
  .heart-yellow { left: 618px; top: 876px; width: 66px; height: 56px; background: var(--yellow-heart); }
  .heart-plum { left: 762px; top: 1040px; width: 170px; height: 148px; background: var(--plum); }
</style>
</head>
<body>
<main class="flyer">
  <svg class="backdrop" width="899" height="1200" viewBox="0 0 899 1200" aria-hidden="true">
    <path d="M0 818 Q0 790 40 790 L46 790 L46 870 Q10 880 0 860 Z" fill="var(--pale-yellow)"/>
    <path d="M0 895 Q30 880 46 910 L46 1160 L30 1200 L0 1200 Z" fill="var(--lilac)" opacity="0.8"/>
    <path d="M230 1200 Q260 1160 330 1165 Q380 1170 380 1200 Z" fill="var(--pale-teal)"/>
    <circle cx="760" cy="22" r="26" fill="var(--lilac)" opacity="0.7"/>
    <circle cx="880" cy="60" r="34" fill="var(--pale-teal)" opacity="0.8"/>
    <circle cx="850" cy="8" r="24" fill="var(--pale-yellow)"/>
  </svg>

  <div class="brand"><span class="brand-dot"></span><span>Silverwattle Care NT</span></div>

  <h1 class="title">
    <span class="title-main">LIVING WITH</span>
    <span class="title-script">Silverwattle Care</span>
  </h1>

  <div class="photo photo-sewing" role="img" aria-label="Photo of a support worker and a boy at a sewing machine"></div>
  <div class="photo photo-craft" role="img" aria-label="Photo of a participant working on a craft project"></div>
  <div class="photo photo-card" role="img" aria-label="Photo of a participant holding a handmade card"></div>
  <div class="partner-badge" role="img" aria-label="Partner badge"></div>
  <div class="heart heart-teal" role="img" aria-label="Heart ornament"></div>

  <section class="services-panel">
    <article class="service service-day">
      <h2 class="service-title">Day Programs <span class="script">for</span><br>Capacity Building</h2>
      <p class="service-body">Our Art and Craft weekly program are perfect for the person that loves to get creative! Whether it be with clay, paint, glass, wool, cans, or pot paints there is something for you! Our cooking cooking program is also up and running! Silverwattle Care also has an amazing shed space where wood and metal programs will be held for skill development and capacity building. Silverwattle Care is here to make all your dreams come true.</p>
    </article>
    <article class="service service-respite">
      <h2 class="service-title">Respite <span class="script">Experiences</span></h2>
      <p class="service-body">We aim to provide memorable and extraordinary experiences, whether that be cooking your favorite meal, going to watch the amazing sunset, going out for a coffee, or going to view what the Northern Territory has to offer. We are here to give you the best experience possible. We also offer transitional housing and MTA.</p>
    </article>
    <article class="service service-community">
      <h2 class="service-title">Community Access &amp;<br>In-Home <span class="script">Supports</span></h2>
      <p class="service-body">Our focus is on finding the best possible services to get all QCSP participants connected with quality services. We aim to provide solutions that make a long-lasting difference. We are servicing all of the Northern Territory. We will support you and assist you to build the skills you need to understand, implement and use your plan.</p>
    </article>
    <article class="service service-employment">
      <h2 class="service-title">Customised <span class="script">Employment</span></h2>
      <p class="service-body">Our amazing psychosocial recovery coaches will work collaboratively with participants, acknowledging that each person is an expert in their own life. The amazing and skilled Silverwattle Care coaches will work with the participant to develop goals, hopes and aspirations.</p>
    </article>
  </section>

  <section class="services-right">
    <article class="service service-workers">
      <h2 class="service-title">Support <span class="script">Workers</span></h2>
      <p class="service-body">Our focus is around best matching participants with our amazing support workers, based on common interests, skills/experience and values. BY best matching our skilled and person &amp; goal-oriented support workers with participants, this ensures to best enable and assist participants to reach their QCSP goals. Supports can be provided in any setting including in the home and community access.</p>
    </article>
    <article class="service service-living">
      <h2 class="service-title">Supported<br>Independent <span class="script">Living</span></h2>
      <p class="service-body">Our specialist Support Coordinator's will assist you to manage challenges in your support environment and ensuring consistent delivery of service.</p>
    </article>
  </section>

  <div class="photo photo-kitchen" role="img" aria-label="Photo of participants cooking together in a kitchen"></div>
  <div class="photo photo-group" role="img" aria-label="Group photo of participants and staff at a celebration"></div>
  <div class="heart heart-yellow" role="img" aria-label="Heart ornament"></div>

  <section class="contact">
    <h2 class="contact-title">Reach Us!</h2>
    <p class="contact-line">
      <svg width="11" height="12" viewBox="0 0 24 24"><path d="M6.6 10.8a15 15 0 0 0 6.6 6.6l2.2-2.2c.3-.3.7-.4 1-.2 1.1.4 2.3.6 3.6.6.6 0 1 .4 1 1V20c0 .6-.4 1-1 1A17 17 0 0 1 3 4c0-.6.4-1 1-1h3.5c.6 0 1 .4 1 1 0 1.3.2 2.5.6 3.6.1.3 0 .7-.2 1z" fill="var(--purple)"/></svg>
      <span>0400-123 456</span>
    </p>
    <p class="contact-line">
      <svg width="10" height="13" viewBox="0 0 24 30"><path d="M12 0a10 10 0 0 0-10 10c0 7.5 10 20 10 20s10-12.5 10-20A10 10 0 0 0 12 0zm0 14a4 4 0 1 1 0-8 4 4 0 0 1 0 8z" fill="var(--purple)"/></svg>
      <span>12/240 Banksia Road,<br>Marlow Vale 0850</span>
    </p>
    <p class="social-title">Find us on <span class="script">Socials</span></p>
    <ul class="social-list"><li></li><li></li><li></li><li></li></ul>
  </section>
  <div class="heart heart-plum" role="img" aria-label="Heart ornament"></div>
</main>
</body>
</html>
```